freelance Nursing care

I'm starting my business as a freelance nurse. With this flyer, i would like to introduce my practice to the doctore as well as to the patients.<br/>my specialization is urodynamics and pelviperineology. i will be working as a consutant in my office and also in home care.<br/><br/>can you make a design with my logo and introduce my description in the flyer.

Target Market(s)

Doctor and patients

Industry/Entity Type

Health Care

Colors

Designer to choose colors to be used in the design.

Requirements
Must have
• - office and home cares services ( see in attache files). you can find it in Offre en soins en cabinet et à domicile
• - Advantage
• - training ( formation)
• -personal coordinate ( coordonnée personnelle)
• -Logo
Nice to have
• attractive design

```html
<!DOCTYPE html>
<html lang="fr">
<head>
<meta charset="utf-8">
<title>Offre en soins – flyer</title>
<link href="https://fonts.googleapis.com/css2?family=Didact+Gothic&family=Roboto:wght@500;700&display=swap" rel="stylesheet">
<style>
  :root{
    --teal:#0aa3a3;
    --teal-dark:#078a8a;
    --ink:#333333;
    --bar:#353535;
    --paper:#ffffff;
    --stage:#3a3a3a;
  }
  *{box-sizing:border-box;margin:0;padding:0}
  html,body{width:1200px;height:1200px;overflow:hidden;background:var(--stage)}
  .flyer{
    position:absolute;left:183px;top:15px;width:907px;height:1273px;
    transform:scale(0.919);transform-origin:top left;
    background:var(--paper);font-family:"Didact Gothic",sans-serif;color:var(--ink);overflow:hidden;
  }
  .hero{position:absolute;left:0;top:0}
  .logo-name{
    position:absolute;left:526px;top:272px;width:160px;text-align:center;
    font-size:21px;color:var(--teal);
  }
  .bar{
    position:absolute;background:var(--bar);color:#fff;
    font-family:"Roboto",sans-serif;font-weight:500;border-radius:0 14px 0 0;
  }
  .bar--offer{left:0;top:450px;width:716px;height:56px;font-size:33px;padding:8px 0 0 50px}
  .bar--adv{left:0;top:802px;width:251px;height:50px;font-size:33px;padding:2px 0 0 52px}
  .bar--form{left:468px;top:802px;width:222px;height:50px;font-size:33px;padding:6px 0 0 31px}
  .divider{position:absolute;left:467px;top:802px;width:3px;height:331px;background:var(--bar)}
  .checks{list-style:none;position:absolute;font-size:16.5px;line-height:19.5px}
  .checks li{position:relative;padding-left:28px}
  .checks svg{position:absolute;left:0;top:1px;width:19px;height:19px}
  .checks--offer{left:50px;top:528px}
  .checks--offer li{margin-bottom:7.2px}
  .checks--adv{left:50px;top:876px;width:372px}
  .checks--form{left:498px;top:876px;width:360px}
  .checks--adv li,.checks--form li{margin-bottom:6.8px}
  .footer{position:absolute;left:0;top:1162px;width:907px;height:111px;background:var(--teal);color:#fff;font-size:16.5px;line-height:20px}
  .pill{
    position:absolute;left:268px;top:1143px;width:398px;height:46px;border-radius:18px;
    background:var(--bar);border:2px solid #fff;color:#fff;text-align:center;
    font-family:"Roboto",sans-serif;font-weight:500;font-size:25px;line-height:41px;
  }
  .address{position:absolute;left:82px;top:32px}
  .address svg{position:absolute;left:-32px;top:-6px}
  .contact{position:absolute;left:673px;top:38px}
  .contact div{position:relative;margin-bottom:10px}
  .contact svg{position:absolute;left:-27px;top:1px}
</style>
</head>
<body>
<div class="flyer">
  <svg class="hero" width="907" height="440" viewBox="0 0 907 440">
    <defs>
      <linearGradient id="garden" x1="0" y1="0" x2="1" y2="1">
        <stop offset="0" stop-color="#7fa56a"/>
        <stop offset="0.45" stop-color="#d9c3b0"/>
        <stop offset="1" stop-color="#a9c96e"/>
      </linearGradient>
      <linearGradient id="portrait" x1="0" y1="0" x2="1" y2="1">
        <stop offset="0" stop-color="#8fb56c"/>
        <stop offset="1" stop-color="#d95a8f"/>
      </linearGradient>
    </defs>
    <rect width="907" height="420" fill="url(#garden)" role="img" aria-label="Photo : une infirmière souriante auprès d'une dame âgée dans un jardin"/>
    <path d="M0,372 C160,430 330,440 520,315 L907,292 L907,440 L0,440 Z" fill="var(--paper)"/>
    <path d="M0,372 C150,412 330,420 530,300 L540,320 C340,445 150,432 0,380 Z" fill="var(--teal)"/>
    <path d="M840,290 L907,296 L907,300 Z" fill="var(--teal)"/>
    <circle cx="760" cy="303" r="110" fill="url(#portrait)" stroke="var(--teal)" stroke-width="4" role="img" aria-label="Photo : infirmière en tenue rose à côté d'un fauteuil roulant"/>
    <circle cx="606" cy="288" r="83" fill="var(--paper)" stroke="var(--teal)" stroke-width="4"/>
  </svg>
  <div class="logo-name">Soins Lien</div>

  <h1 class="bar bar--offer">Offre en soins en cabinet et à domicile</h1>
  <ul class="checks checks--offer">
    <li><svg viewBox="0 0 20 20"><path d="M16.5 9.5A7 7 0 1 1 13 3.6" fill="none" stroke="#0aa3a3" stroke-width="2.2"/><path d="M6 9.5l3.3 3.3L18 3.8" fill="none" stroke="#0aa3a3" stroke-width="2.6"/></svg>Enseignement en soins d’incontinence (condoms, tampons, irrigation anale, protection…etc.)</li>
    <li><svg viewBox="0 0 20 20"><path d="M16.5 9.5A7 7 0 1 1 13 3.6" fill="none" stroke="#0aa3a3" stroke-width="2.2"/><path d="M6 9.5l3.3 3.3L18 3.8" fill="none" stroke="#0aa3a3" stroke-width="2.6"/></svg>Enseignement à l’auto-sondage</li>
    <li><svg viewBox="0 0 20 20"><path d="M16.5 9.5A7 7 0 1 1 13 3.6" fill="none" stroke="#0aa3a3" stroke-width="2.2"/><path d="M6 9.5l3.3 3.3L18 3.8" fill="none" stroke="#0aa3a3" stroke-width="2.6"/></svg>Changement de sonde sus pubien ou transurétrale</li>
    <li><svg viewBox="0 0 20 20"><path d="M16.5 9.5A7 7 0 1 1 13 3.6" fill="none" stroke="#0aa3a3" stroke-width="2.2"/><path d="M6 9.5l3.3 3.3L18 3.8" fill="none" stroke="#0aa3a3" stroke-width="2.6"/></svg>Enseignement de neurostimulation tibiale, intravaginale, vagale.</li>
    <li><svg viewBox="0 0 20 20"><path d="M16.5 9.5A7 7 0 1 1 13 3.6" fill="none" stroke="#0aa3a3" stroke-width="2.2"/><path d="M6 9.5l3.3 3.3L18 3.8" fill="none" stroke="#0aa3a3" stroke-width="2.6"/></svg>Dilatations par -sondage</li>
    <li><svg viewBox="0 0 20 20"><path d="M16.5 9.5A7 7 0 1 1 13 3.6" fill="none" stroke="#0aa3a3" stroke-width="2.2"/><path d="M6 9.5l3.3 3.3L18 3.8" fill="none" stroke="#0aa3a3" stroke-width="2.6"/></svg>Pansements etc</li>
    <li><svg viewBox="0 0 20 20"><path d="M16.5 9.5A7 7 0 1 1 13 3.6" fill="none" stroke="#0aa3a3" stroke-width="2.2"/><path d="M6 9.5l3.3 3.3L18 3.8" fill="none" stroke="#0aa3a3" stroke-width="2.6"/></svg>Sous Mandat : Effectuer le bilan urodynamique (BUD) en collaboration avec médecin spécialiste.</li>
    <li><svg viewBox="0 0 20 20"><path d="M16.5 9.5A7 7 0 1 1 13 3.6" fill="none" stroke="#0aa3a3" stroke-width="2.2"/><path d="M6 9.5l3.3 3.3L18 3.8" fill="none" stroke="#0aa3a3" stroke-width="2.6"/></svg>Pose de sonde nasogastrique, pose VVP, PAC, perfusion des ATB etc…</li>
    <li><svg viewBox="0 0 20 20"><path d="M16.5 9.5A7 7 0 1 1 13 3.6" fill="none" stroke="#0aa3a3" stroke-width="2.2"/><path d="M6 9.5l3.3 3.3L18 3.8" fill="none" stroke="#0aa3a3" stroke-width="2.6"/></svg>Contrôle de santé, préparation de semainier</li>
  </ul>

  <h2 class="bar bar--adv">Avantages</h2>
  <h2 class="bar bar--form">Formation</h2>
  <div class="divider"></div>

  <ul class="checks checks--adv">
    <li><svg viewBox="0 0 20 20"><path d="M16.5 9.5A7 7 0 1 1 13 3.6" fill="none" stroke="#0aa3a3" stroke-width="2.2"/><path d="M6 9.5l3.3 3.3L18 3.8" fill="none" stroke="#0aa3a3" stroke-width="2.6"/></svg>Offrir un suivi personnalisé et de qualité à chaque besoin, avec la même intervenante ayant une expertise du domaine de compétence.</li>
    <li><svg viewBox="0 0 20 20"><path d="M16.5 9.5A7 7 0 1 1 13 3.6" fill="none" stroke="#0aa3a3" stroke-width="2.2"/><path d="M6 9.5l3.3 3.3L18 3.8" fill="none" stroke="#0aa3a3" stroke-width="2.6"/></svg>Promouvoir la plus grande autonomie et la meilleure qualité de vie</li>
    <li><svg viewBox="0 0 20 20"><path d="M16.5 9.5A7 7 0 1 1 13 3.6" fill="none" stroke="#0aa3a3" stroke-width="2.2"/><path d="M6 9.5l3.3 3.3L18 3.8" fill="none" stroke="#0aa3a3" stroke-width="2.6"/></svg>Conseils et promotion de la santé</li>
    <li><svg viewBox="0 0 20 20"><path d="M16.5 9.5A7 7 0 1 1 13 3.6" fill="none" stroke="#0aa3a3" stroke-width="2.2"/><path d="M6 9.5l3.3 3.3L18 3.8" fill="none" stroke="#0aa3a3" stroke-width="2.6"/></svg>Intégrer le plus rapidement possible le domicile après une hospitalisation</li>
    <li><svg viewBox="0 0 20 20"><path d="M16.5 9.5A7 7 0 1 1 13 3.6" fill="none" stroke="#0aa3a3" stroke-width="2.2"/><path d="M6 9.5l3.3 3.3L18 3.8" fill="none" stroke="#0aa3a3" stroke-width="2.6"/></svg>Contribuer au développement de réseaux de soin.</li>
  </ul>

  <ul class="checks checks--form">
    <li><svg viewBox="0 0 20 20"><path d="M16.5 9.5A7 7 0 1 1 13 3.6" fill="none" stroke="#0aa3a3" stroke-width="2.2"/><path d="M6 9.5l3.3 3.3L18 3.8" fill="none" stroke="#0aa3a3" stroke-width="2.6"/></svg>Participation aux divers congrès d’urologie (SUPEL, ANUP, CORA, Symposium de Neuro urologie CHRV)</li>
    <li><svg viewBox="0 0 20 20"><path d="M16.5 9.5A7 7 0 1 1 13 3.6" fill="none" stroke="#0aa3a3" stroke-width="2.2"/><path d="M6 9.5l3.3 3.3L18 3.8" fill="none" stroke="#0aa3a3" stroke-width="2.6"/></svg>Diplôme université d’urodynamique et pelvi-périnéologie</li>
    <li><svg viewBox="0 0 20 20"><path d="M16.5 9.5A7 7 0 1 1 13 3.6" fill="none" stroke="#0aa3a3" stroke-width="2.2"/><path d="M6 9.5l3.3 3.3L18 3.8" fill="none" stroke="#0aa3a3" stroke-width="2.6"/></svg>Expériences divers (Oncologie, Gynécologie, Urodynamique et pelvi-périnéologie)</li>
    <li><svg viewBox="0 0 20 20"><path d="M16.5 9.5A7 7 0 1 1 13 3.6" fill="none" stroke="#0aa3a3" stroke-width="2.2"/><path d="M6 9.5l3.3 3.3L18 3.8" fill="none" stroke="#0aa3a3" stroke-width="2.6"/></svg>Infirmière HES depuis 10 ans</li>
  </ul>

  <footer class="footer">
    <div class="address">
      <svg width="22" height="26" viewBox="0 0 22 26"><path d="M11 2a7 7 0 0 1 7 7c0 5-7 11-7 11S4 14 4 9a7 7 0 0 1 7-7z" fill="none" stroke="#fff" stroke-width="1.6"/><circle cx="11" cy="9" r="2.5" fill="none" stroke="#fff" stroke-width="1.6"/><ellipse cx="11" cy="23" rx="8" ry="2" fill="none" stroke="#fff" stroke-width="1.2"/></svg>
      Consultation au cabinet<br>Clinique des Tilleuls, Rue des Vergers 12<br>1000 Valmont
    </div>
    <div class="contact">
      <div><svg width="18" height="22" viewBox="0 0 18 22"><path d="M5 2c-2 1-3 3-3 6 0 5 4 11 8 12 1 0 2-1 3-2l-3-4-2 1c-1-2-2-5-2-7l2-1L6 2z" fill="#fff"/></svg>07-5100-0420</div>
      <div><svg width="20" height="14" viewBox="0 0 20 14"><rect x="1" y="1" width="18" height="12" fill="#fff"/><path d="M1 1l9 7 9-7" fill="none" stroke="#0aa3a3" stroke-width="1.4"/></svg>contact@soins-lien.ch</div>
    </div>
  </footer>
  <div class="pill">Coordonnées personnelles</div>
</div>
</body>
</html>
```